Lanternfield Disability - Social Security Disability Attorneys

Our company is expanding to attract clients nationwide for our social security disability practice. We have a logo, but I am looking for a creative and elegant letterhead that projects an image of being technologically advanced but still professional enough for the legal field. I am looking for the "wow factor" combined with this is still professional enough for a law practice.

Requesting letterhead and business card design
Updates

Had to update and change the logo. The previous logo had a typo. Please send updates with the new logo for consideration. The letterhead and business cards should be professional enough to be used for a law firm. Thanks.

Industry/Entity Type

Law Practice, Law Firm, Healthcare Industry, Government

Colors

Designer to choose colors to be used in the design.

Requirements
Nice to have
• **Please create a vertical design for the business card**

```html
<!DOCTYPE html>
<html lang="en">
<head>
<meta charset="utf-8">
<title>Lanternfield Disability – Letterhead and Business Card</title>
<link href="https://fonts.googleapis.com/css2?family=Raleway:wght@400;500;600;700&display=swap" rel="stylesheet">
<style>
  :root{
    --blue:#1a78e6;
    --blue-light:#12a9ec;
    --blue-deep:#0a5fe0;
    --orange:#f7830f;
    --ink:#3a3a3a;
    --ink-soft:#555;
    --paper:#ffffff;
    --backdrop:#e6e7ea;
    --rule:#e3e3e3;
  }
  *{box-sizing:border-box;margin:0;padding:0}
  html,body{width:1200px;height:1000px;overflow:hidden}
  body{background:var(--backdrop);font-family:"Raleway",sans-serif;color:var(--ink);position:relative}

  .letterhead{position:absolute;left:92px;top:147px;width:572px;height:741px;background:var(--paper);box-shadow:0 6px 18px rgba(0,0,0,.18);overflow:hidden}
  .brand-name{position:absolute;left:0;right:0;text-align:center;color:var(--blue);font-family:"Raleway",sans-serif;font-weight:600;letter-spacing:.5px}
  .letterhead .brand-name{top:82px;font-size:30px}
  .brand-mark{display:inline-block;width:.5em;height:.5em;border-radius:50%;background:var(--blue);margin-right:.35em;vertical-align:.08em}

  .block{position:absolute;left:44px;width:489px;font-size:9.2px;line-height:15px;color:var(--ink-soft)}
  .label{font-weight:700;color:var(--ink)}
  .subject{top:144px}
  .salutation{top:220px}
  .body-text{text-align:justify}
  .p1{top:250px}.p2{top:340px}.p3{top:430px}
  .signoff{top:549px}

  .contact-tab{position:absolute;left:0;top:621px;width:19px;height:84px;background:linear-gradient(180deg,var(--blue-light),var(--blue-deep));border-radius:0 10px 10px 0}
  .tab-icon{position:absolute;left:3px;width:12px;height:12px;border-radius:50%;background:#fff;display:flex;align-items:center;justify-content:center}
  .contact-list{position:absolute;left:28px;top:632px;font-size:11px;line-height:21px;color:var(--ink)}
  .footer-bands{position:absolute;left:0;bottom:0;width:572px;height:22px}
  .site{position:absolute;left:135px;bottom:1px;font-size:8.5px;letter-spacing:3px;color:#fff}

  .card{position:absolute;left:738px;width:370px;height:218px;background:var(--paper);border-radius:23px;box-shadow:0 6px 18px rgba(0,0,0,.18);overflow:hidden}
  .card-front{top:283px}
  .card-front .brand-name{top:96px;font-size:22px}
  .card-back{top:517px}
  .holder{position:absolute;left:43px;top:92px}
  .holder-name{font-size:16px;font-weight:700;color:var(--ink);line-height:18px}
  .holder-role{font-size:12px;color:var(--ink-soft);line-height:15px}
  .divider{position:absolute;left:176px;top:64px;width:1px;height:86px;background:var(--rule)}
  .card-contact{position:absolute;left:194px;display:flex;align-items:center;font-size:11px;color:var(--ink)}
  .card-contact .dot{width:15px;height:15px;border-radius:50%;background:linear-gradient(180deg,var(--blue-light),var(--blue-deep));display:flex;align-items:center;justify-content:center;margin-right:13px}
  .c1{top:64px}.c2{top:90px}.c3{top:115px}
  .card-bands{position:absolute;left:0;bottom:0;width:370px;height:15px}
</style>
</head>
<body>

<section class="letterhead">
  <div class="brand-name"><span class="brand-mark"></span>Lanternfield Disability</div>

  <div class="block subject"><div class="label">SUBJECT</div>Lorem ipsum dolor sit amet</div>
  <div class="block salutation label">Dear Person</div>

  <p class="block body-text p1">Lorem ipsum dolor sit amet, consectetuer adipiscing elit, sed diam nonummy nibh euismod tincidunt ut laoreet dolore magna aliquam erat volutpat. Ut wisi enim ad minim veniam, quis nostrud exerci tation ullamcorper suscipit lobortis nisl ut aliquip ex ea commodo conse. Lorem ipsum dolor sit amet, consectetuer adipiscing elit, sed diam nonummy nibh euismod tincidunt ut laoreet dolore magna aliquam erat volutpat. Ut wisi enim ad minim veniam, quis nostrud exerci tation ullamcorper suscipit lobortis nisl ut aliquip ex ea commodo conse.</p>
  <p class="block body-text p2">Lorem ipsum dolor sit amet, consectetuer adipiscing elit, sed diam nonummy nibh euismod tincidunt ut laoreet dolore magna aliquam erat volutpat. Ut wisi enim ad minim veniam, quis nostrud exerci tation ullamcorper suscipit lobortis nisl ut aliquip ex ea commodo conse. Lorem ipsum dolor sit amet, consectetuer adipiscing elit, sed diam nonummy nibh euismod tincidunt ut laoreet dolore magna aliquam erat volutpat. Ut wisi enim ad minim veniam, quis nostrud exerci tation ullamcorper suscipit lobortis nisl ut aliquip ex ea commodo conse.</p>
  <p class="block body-text p3">Lorem ipsum dolor sit amet, consectetuer adipiscing elit, sed diam nonummy nibh euismod tincidunt ut laoreet dolore magna aliquam erat volutpat. Ut wisi enim ad minim veniam, quis nostrud exerci tation ullamcorper suscipit lobortis nisl ut aliquip ex ea commodo conse. Lorem ipsum dolor sit amet, consectetuer adipiscing elit, sed diam nonummy nibh euismod tincidunt ut laoreet dolore magna aliquam erat volutpat. Ut wisi enim ad minim veniam, quis nostrud exerci tation ullamcorper suscipit lobortis nisl ut aliquip ex ea commodo conse.</p>

  <div class="block signoff"><div class="label">Marcus Ellery</div>Managing Director</div>

  <div class="contact-tab">
    <span class="tab-icon" style="top:14px"><svg width="7" height="7" viewBox="0 0 10 10"><path d="M2 1l2 2-1 1.2c.6 1.2 1.6 2.2 2.8 2.8L7 6l2 2-1.3 1.3C4.5 9 1 5.5.7 2.3z" fill="var(--blue)"/></svg></span>
    <span class="tab-icon" style="top:36px"><svg width="7" height="6" viewBox="0 0 10 8"><rect x=".5" y=".5" width="9" height="7" rx="1" fill="var(--blue)"/><path d="M1 1l4 3.5L9 1" stroke="#fff" fill="none"/></svg></span>
    <span class="tab-icon" style="top:57px"><svg width="6" height="8" viewBox="0 0 8 11"><path d="M4 0a4 4 0 014 4c0 3-4 7-4 7S0 7 0 4a4 4 0 014-4z" fill="var(--blue)"/><circle cx="4" cy="4" r="1.4" fill="#fff"/></svg></span>
  </div>
  <div class="contact-list">
    <div>012345678910</div>
    <div>yourmail@lanternfield.com</div>
    <div>your office address goes here</div>
  </div>

  <svg class="footer-bands" viewBox="0 0 572 22" preserveAspectRatio="none">
    <defs><linearGradient id="lhBlue" x1="0" x2="1"><stop offset="0" stop-color="#12a9ec"/><stop offset="1" stop-color="#0a5fe0"/></linearGradient></defs>
    <polygon points="0,8 408,8 398,22 0,22" fill="var(--orange)"/>
    <polygon points="419,0 572,0 572,22 404,22" fill="url(#lhBlue)"/>
  </svg>
  <div class="site">WWW.YOURWEBSITE.COM</div>
</section>

<section class="card card-front">
  <div class="brand-name"><span class="brand-mark"></span>Lanternfield Disability</div>
</section>

<section class="card card-back">
  <div class="holder">
    <div class="holder-name">Marcus Ellery</div>
    <div class="holder-role">Managing Director</div>
  </div>
  <div class="divider"></div>
  <div class="card-contact c1"><span class="dot"><svg width="8" height="8" viewBox="0 0 10 10"><path d="M2 1l2 2-1 1.2c.6 1.2 1.6 2.2 2.8 2.8L7 6l2 2-1.3 1.3C4.5 9 1 5.5.7 2.3z" fill="#fff"/></svg></span>012345678910</div>
  <div class="card-contact c2"><span class="dot"><svg width="8" height="6" viewBox="0 0 10 8"><rect x=".5" y=".5" width="9" height="7" rx="1" fill="#fff"/><path d="M1 1l4 3.5L9 1" stroke="var(--blue)" fill="none"/></svg></span>yourmail@lanternfield.com</div>
  <div class="card-contact c3"><span class="dot"><svg width="6" height="8" viewBox="0 0 8 11"><path d="M4 0a4 4 0 014 4c0 3-4 7-4 7S0 7 0 4a4 4 0 014-4z" fill="#fff"/><circle cx="4" cy="4" r="1.4" fill="var(--blue)"/></svg></span>your office address goes here</div>
  <svg class="card-bands" viewBox="0 0 370 15" preserveAspectRatio="none">
    <defs><linearGradient id="cdBlue" x1="0" x2="1"><stop offset="0" stop-color="#12a9ec"/><stop offset="1" stop-color="#0a5fe0"/></linearGradient></defs>
    <polygon points="0,5 244,5 236,15 0,15" fill="var(--orange)"/>
    <polygon points="254,0 370,0 370,15 242,15" fill="url(#cdBlue)"/>
  </svg>
</section>

</body>
</html>
```